New modern and animated Design needed for a portal login site (Relayon Portal)

Relayon is software for market communication B2B & EAI.
We need a modern look for a Relayon Portal login site. We prefer a full size use for the background design of the login-page, with animation.
The name of the site is “Relayon Langzeitarchiv”, what should appear as text. Further there is space needed for the login name and password.
Responsive Design is required.
We have a new Relayon logo (find attached), that can be used for the animation, for example but not necessarily.
Feel free to visit our website for inspiration (colours etc.): www.vormelsysteme.de.
Updates

Reason: Can you please animate the backgraound and send links to view it.

Reason: there is aproblem with pixelforum - we acually cannot view any designs

Target Market(s)

energy sector, IT

Industry/Entity Type

Communication

Number of Pages Required

1 page

Font styles to use
Sans Serif

Colors

Designer to choose colors to be used in the design.

Requirements
Must have
• fullscreen background design (like "onepager"),
• animated (infinity), not to much action
• the only text that is needed is "Relayon Langzeitarchiv" (in front) and the login details: "Benutzername" (+ space for the username (free position)) and "Paswort" (+ space for the password (free position))
Nice to have
• maybe shades of blue, or colours, like the ones used on our website and logo (vormel systeme) or Relayon icon (files named "asset")
• animation can also be a film that starts over and over again (note: The up half of the page www.brunostafa.de is one example, which is nice to watch - but here it is not necessary to use a movie)

```html
<!DOCTYPE html>
<html lang="de">
<head>
<meta charset="utf-8">
<title>Relayon Langzeitarchiv – Login</title>
<link rel="stylesheet" href="https://fonts.googleapis.com/css2?family=Mulish:wght@400;600;700&display=swap">
<style>
  :root {
    --night: #050d1c;
    --deep: #0a1c3a;
    --steel: #1d4a86;
    --haze: #2f64a8;
    --hex: #1657a6;
    --hex-light: #3d7ec2;
    --action: #1ea7e4;
    --footer: #0b2f5e;
    --white: #ffffff;
    --field-text: #8a8f96;
  }
  * { box-sizing: border-box; margin: 0; padding: 0; }
  html, body { width: 1200px; height: 756px; overflow: hidden; background: var(--night); }
  body { font-family: "Mulish", Arial, sans-serif; color: var(--white); }

  .login-page { position: relative; width: 1200px; height: 756px; overflow: hidden; }

  .backdrop {
    position: absolute; inset: 0 0 79px 0;
    background:
      radial-gradient(ellipse 420px 260px at 300px 520px, rgba(120,130,150,0.35), transparent 70%),
      radial-gradient(ellipse 700px 380px at 250px 200px, rgba(47,100,168,0.55), transparent 75%),
      linear-gradient(180deg, var(--steel) 0%, var(--deep) 45%, var(--night) 100%);
  }

  .brand {
    position: absolute; left: 105px; top: 48px;
    font-weight: 400; font-size: 58px; line-height: 56px; letter-spacing: -1px;
    color: var(--white);
  }
  .brand span { display: block; }
  .brand span + span { padding-left: 66px; }

  .site-title {
    position: absolute; left: 105px; top: 276px;
    font-weight: 700; font-size: 47px; line-height: 56px; letter-spacing: 0.3px;
  }

  .globe { position: absolute; left: 0; top: 0; }

  .login-form { position: absolute; left: 693px; top: 228px; width: 272px; }
  .field {
    display: block; width: 100%; height: 46px; margin-bottom: 17px;
    border: 1px solid #d6dbe2; border-radius: 2px; background: var(--white);
    padding: 0 14px; font: 400 14px "Mulish", Arial, sans-serif; color: var(--field-text);
  }
  .login-button {
    display: block; width: 100%; height: 58px; margin-top: 0;
    border: 0; border-radius: 2px; background: var(--action);
    font: 400 24px "Mulish", Arial, sans-serif; color: var(--white); letter-spacing: 0.5px;
  }

  .site-footer {
    position: absolute; left: 0; bottom: 0; width: 1200px; height: 79px;
    background: var(--footer);
  }
  .copyright { position: absolute; left: 105px; top: 27px; font-weight: 600; font-size: 20px; }
  .social-links { position: absolute; left: 875px; top: 18px; display: flex; gap: 16px; }
  .social-links span {
    width: 42px; height: 42px; border: 2px solid var(--white); border-radius: 50%;
  }
</style>
</head>
<body>
<main class="login-page">
  <div class="backdrop" role="img" aria-label="Dunkelblaue Stadtsilhouette mit einer ausgestreckten Hand, die auf einen digitalen Globus zeigt"></div>

  <div class="brand"><span>vormel</span><span>systeme</span></div>

  <h1 class="site-title">Relayon<br>Langzeitarchiv</h1>

  <svg class="globe" width="1200" height="677" viewBox="0 0 1200 677">
    <defs>
      <radialGradient id="globe-fill" cx="50%" cy="45%" r="55%">
        <stop offset="0" stop-color="#2a5a96"/>
        <stop offset="0.7" stop-color="#12305e"/>
        <stop offset="1" stop-color="#6d8fbf"/>
      </radialGradient>
    </defs>
    <circle cx="880" cy="312" r="248" fill="url(#globe-fill)" role="img" aria-label="Vernetzte Weltkugel mit leuchtenden Kontinenten"/>
    <polygon points="630,320 712,153 968,153 1050,320 968,487 712,487" fill="var(--hex)" opacity="0.92"/>
    <polygon points="712,153 968,153 1050,320 968,487" fill="var(--hex-light)" opacity="0.25"/>
  </svg>

  <form class="login-form">
    <input class="field" type="text" placeholder="Benutzername">
    <input class="field" type="password" placeholder="Passwort">
    <button class="login-button" type="button">LOGIN</button>
  </form>

  <footer class="site-footer">
    <p class="copyright">© 2017 Company Name All right reserved</p>
    <div class="social-links"><span></span><span></span><span></span><span></span></div>
  </footer>
</main>
</body>
</html>
```